The Velvet Magpie business card

I need a business card for my makeup artist business. I specialise in bridal, glamour, formal and special occasion makeup.
I am a mobile makeup artist who caters for every from nowra to sydney.
I do the following services:
Bridal makeup
airbrush makeup
special occasion
formals
hens nights/ girls night
makeup lesson
makeup for all ages from flower girl to Nanna of the bride!
photoshoot makeup
SPFX

I would like the card to portray a very professional sleek makeup business. I would also like another version of the card directed especially towards brides.

Please see my website to understand colours etc www.thevelvetmagpie.com

The Velvet Magpie
Professional Makeup Artist
Marisol Dunkel
0471829304
info@thevelvetmagpie.com
www.thevelvetmagpie.com
www.friendnest.com/thevelvetmagpie

```html
<!DOCTYPE html>
<html lang="en">
<head>
<meta charset="utf-8">
<title>The Velvet Magpie – Business Card</title>
<link rel="stylesheet" href="https://fonts.googleapis.com/css2?family=Didact+Gothic&display=swap">
<style>
  :root {
    --magenta: #c71f78;
    --peach: #efc6ab;
    --cream: #f6dccb;
    --blush: #f6d6e3;
    --ink: #2f2f2f;
    --grey: #555555;
    --rule: #9a9a9a;
    --paper: #ffffff;
    --backdrop: #ece9e5;
  }
  * { box-sizing: border-box; margin: 0; padding: 0; }
  html, body {
    width: 1200px;
    height: 784px;
    overflow: hidden;
  }
  body {
    position: relative;
    background: var(--backdrop);
    font-family: "Didact Gothic", "Century Gothic", sans-serif;
  }

  .card {
    position: absolute;
    width: 640px;
    height: 366px;
    overflow: hidden;
    box-shadow: 0 6px 18px rgba(0,0,0,0.18);
  }

  /* Services side */
  .card--services {
    left: 40px;
    top: 44px;
    background: var(--magenta);
  }
  .card--services .brand {
    position: absolute;
    left: 50px;
    top: 52px;
    color: var(--cream);
    font-size: 34px;
    letter-spacing: 3px;
    text-transform: uppercase;
    white-space: nowrap;
  }
  .service-list {
    position: absolute;
    left: 58px;
    top: 112px;
    list-style: disc;
    color: var(--cream);
    font-size: 16px;
    line-height: 22px;
    padding-left: 14px;
  }
  .card--services .portrait {
    position: absolute;
    right: 0;
    top: 0;
    width: 270px;
    height: 366px;
    background: linear-gradient(200deg, var(--cream) 0%, var(--peach) 45%, #d79a86 75%, var(--magenta) 100%);
    -webkit-mask-image: linear-gradient(90deg, transparent 0%, #000 28%);
            mask-image: linear-gradient(90deg, transparent 0%, #000 28%);
  }

  /* Contact side */
  .card--contact {
    left: 510px;
    top: 376px;
    background: var(--paper);
  }
  .card--contact .ornament {
    position: absolute;
    right: 0;
    top: 0;
    width: 220px;
    height: 300px;
    background: radial-gradient(ellipse at 85% 20%, var(--blush) 0%, rgba(246,214,227,0.6) 45%, rgba(255,255,255,0) 75%);
  }
  .card--contact .portrait {
    position: absolute;
    left: 42px;
    top: 80px;
    width: 126px;
    height: 126px;
    background: linear-gradient(160deg, #f2d2dd 0%, #e48db4 45%, var(--magenta) 100%);
  }
  .card--contact .brand {
    position: absolute;
    left: 180px;
    top: 88px;
    color: var(--magenta);
    font-size: 33px;
    letter-spacing: 3px;
    text-transform: uppercase;
    white-space: nowrap;
  }
  .card--contact .tagline {
    position: absolute;
    left: 180px;
    top: 144px;
    width: 400px;
    border-top: 1px solid var(--rule);
    padding-top: 6px;
    color: var(--grey);
    font-size: 17px;
    letter-spacing: 4px;
  }
  .holder {
    position: absolute;
    left: 112px;
    top: 222px;
    color: var(--magenta);
    font-size: 19px;
  }
  .contact-list {
    position: absolute;
    left: 120px;
    top: 250px;
    list-style: none;
    color: var(--ink);
    font-size: 17px;
    line-height: 23px;
  }
  .contact-list li {
    display: flex;
    align-items: center;
    gap: 8px;
  }
  .contact-list svg {
    width: 16px;
    height: 16px;
    flex: none;
    fill: var(--magenta);
  }
</style>
</head>
<body>

<section class="card card--services" aria-label="Card back: services">
  <div class="portrait" role="img" aria-label="Stylised portrait illustration of the makeup artist in peach and pink tones"></div>
  <p class="brand">The Velvet Magpie</p>
  <ul class="service-list">
    <li>Bridal makeup</li>
    <li>airbrush makeup</li>
    <li>special occasion</li>
    <li>formals</li>
    <li>hens nights/ girls night</li>
    <li>makeup lesson</li>
    <li>makeup for all ages from flower girl to Nanna of the bride!</li>
    <li>photoshoot makeup</li>
    <li>SPFX</li>
  </ul>
</section>

<section class="card card--contact" aria-label="Card front: contact details">
  <div class="ornament" role="img" aria-label="Soft pink floral leaf ornament"></div>
  <div class="portrait" role="img" aria-label="Square stylised portrait illustration of the makeup artist in pink tones"></div>
  <p class="brand">The Velvet Magpie</p>
  <p class="tagline">Professional Makeup Artist</p>

  <p class="holder">Marisol Dunkel</p>
  <ul class="contact-list">
    <li>
      <svg viewBox="0 0 16 16" aria-hidden="true"><path d="M3.2 1.5l2.3 2.6-1.3 1.8c.9 2 2.4 3.6 4.4 4.6l1.8-1.3 2.6 2.2-1.5 2.3C6.6 13.5 2.3 9.2 1 4l2.2-2.5z"/></svg>
      <span>0471829304</span>
    </li>
    <li>
      <svg viewBox="0 0 16 16" aria-hidden="true"><path d="M1 4h14v9H1z" fill="none" stroke="#c71f78" stroke-width="1.6"/><path d="M1.5 4.5L8 9l6.5-4.5" fill="none" stroke="#c71f78" stroke-width="1.6"/></svg>
      <span>info@thevelvetmagpie.com</span>
    </li>
    <li>
      <svg viewBox="0 0 16 16" aria-hidden="true"><g fill="none" stroke="#c71f78" stroke-width="1.4"><circle cx="8" cy="8" r="6.5"/><ellipse cx="8" cy="8" rx="3" ry="6.5"/><path d="M1.5 8h13M2.5 4.8h11M2.5 11.2h11"/></g></svg>
      <span>www.thevelvetmagpie.com</span>
    </li>
    <li>
      <svg viewBox="0 0 16 16" aria-hidden="true"><rect x="1" y="1" width="14" height="14" rx="2"/></svg>
      <span>www.friendnest.com/thevelvetmagpie</span>
    </li>
  </ul>
</section>

</body>
</html>
```